IT Consulting Business Card Design

We need a business card on our company name....which is a IT consulting and staffing company. We also train masters graduates in various IT courses. 70% of the time these cards will be handed out to the graduate students at the universities. 30% for our clients and business partners. We are uploading our company logo...would like to see something that matches our logo or blends with it. Please visit www.brightvaleworks.com for more details on logo and colors.

Target Market(s)

70% of the time these cards will be handed out to the graduate students at the universities. 30% for our clients and business partners.

Industry/Entity Type

Business

Contact Information for Business Card

Ravi Kondamuri
Vice-President
Bright Vale Works Inc
3807 Morrow Lane, Suite 412
East Brookridge, NJ 07315
ravi@brightvaleworks.com
Office : 1-866-219-3840 X 515
Cell number : 732-581-9034

Requirements
Nice to have
• may be company logo and name on the back of the card and detials on the other side...just a thought..!!

```html
<!DOCTYPE html>
<html lang="en">
<head>
<meta charset="utf-8">
<title>Bright Vale Works – Business Card</title>
<link rel="stylesheet" href="https://fonts.googleapis.com/css2?family=Arimo:wght@400;700&family=Questrial&display=swap">
<style>
  :root {
    --page-bg: #f4f4f4;
    --card-white: #ffffff;
    --card-white-edge: #ececec;
    --brand-red: #d8222a;
    --ink-dark: #2b2b2d;
    --panel-dark: #2a2b2e;
    --panel-darker: #1f2022;
    --text-light: #f2f2f2;
    --faint-mark: rgba(150, 60, 50, 0.28);
  }
  * { box-sizing: border-box; margin: 0; padding: 0; }
  html, body {
    width: 1200px; height: 900px; overflow: hidden;
    background: var(--page-bg);
  }
  .stage {
    position: relative; width: 1200px; height: 900px;
  }
  .card {
    position: absolute; top: 300px;
    width: 520px; height: 300px;
    border-radius: 22px; overflow: hidden;
    box-shadow: 0 10px 24px rgba(0,0,0,0.18);
  }
  .card--front { left: 50px; background: var(--card-white); }
  .card--back {
    left: 630px;
    background: linear-gradient(180deg, var(--panel-dark), var(--panel-darker));
  }

  /* front: upper white area */
  .front-top {
    position: absolute; inset: 0 0 auto 0; height: 138px;
    background: linear-gradient(180deg, var(--card-white-edge), var(--card-white) 40%);
  }
  .person {
    position: absolute; right: 28px; top: 20px; text-align: right;
    font-family: "Arimo", Arial, sans-serif;
  }
  .person__name { color: var(--brand-red); font-weight: 700; font-size: 19px; }
  .person__title { color: var(--ink-dark); font-size: 13px; margin-top: 2px; }
  .brand {
    position: absolute; left: 22px; top: 58px;
    display: flex; align-items: center; gap: 18px;
  }
  .brand__dot {
    width: 66px; height: 66px; border-radius: 50%;
    background: var(--brand-red);
  }
  .brand__name {
    font-family: "Arimo", Arial, sans-serif; font-weight: 700;
    font-size: 30px; color: var(--ink-dark); letter-spacing: -0.5px;
  }

  .red-band {
    position: absolute; left: 0; right: 0; top: 138px; height: 14px;
    background: var(--brand-red);
  }
  .front-bottom {
    position: absolute; left: 0; right: 0; top: 152px; bottom: 0;
    background: linear-gradient(180deg, var(--panel-dark), var(--panel-darker));
    padding: 10px 24px;
    font-family: "Questrial", "Century Gothic", sans-serif;
  }
  .company-legal {
    color: var(--brand-red); font-family: "Arimo", Arial, sans-serif;
    font-size: 14px; margin-bottom: 10px;
  }
  .contact-list { list-style: none; color: var(--text-light); font-size: 14px; line-height: 21px; }
  .contact-list li { display: flex; align-items: center; gap: 6px; }
  .contact-list svg { width: 12px; height: 12px; fill: var(--brand-red); flex: none; }
  .contact-list .indent { padding-left: 18px; }

  /* back */
  .back-mark {
    position: absolute; left: 150px; top: 30px;
    width: 240px; height: 240px; border-radius: 50%;
    background: var(--faint-mark);
  }
  .back-url {
    position: absolute; left: 0; right: 0; top: 138px; text-align: center;
    font-family: "Questrial", "Century Gothic", sans-serif;
    color: var(--text-light); font-size: 19px; letter-spacing: 6px;
  }
</style>
</head>
<body>
<main class="stage">
  <section class="card card--front" aria-label="Card front">
    <div class="front-top">
      <div class="person">
        <p class="person__name">Ravi Kondamuri</p>
        <p class="person__title">Vice-President</p>
      </div>
      <div class="brand">
        <span class="brand__dot"></span>
        <span class="brand__name">BRIGHT VALE WORKS</span>
      </div>
    </div>
    <div class="red-band"></div>
    <div class="front-bottom">
      <p class="company-legal">Bright Vale Works Inc</p>
      <ul class="contact-list">
        <li><svg viewBox="0 0 12 12"><path d="M2 1l2 0 1 3-1.5 1a6 6 0 0 0 3.5 3.5L8 7l3 1v2a1 1 0 0 1-1 1A9 9 0 0 1 1 2a1 1 0 0 1 1-1z"/></svg>1-866-219-3840 X 515</li>
        <li><svg viewBox="0 0 12 12"><rect x="3" y="0.5" width="6" height="11" rx="1"/></svg>732-581-9034</li>
        <li><svg viewBox="0 0 12 12"><path d="M1 2.5h10v7H1z M1 2.5l5 4 5-4" stroke="#2a2b2e" stroke-width="0.8"/></svg>ravi@brightvaleworks.com</li>
        <li><svg viewBox="0 0 12 12"><path d="M6 1l5.5 5H10v5H7.5V8h-3v3H2V6H0.5z"/></svg>3807 Morrow Lane,</li>
        <li class="indent">Suite 412 East Brookridge, NJ 07315</li>
      </ul>
    </div>
  </section>

  <section class="card card--back" aria-label="Card back">
    <div class="back-mark"></div>
    <p class="back-url">www.brightvaleworks.com</p>
  </section>
</main>
</body>
</html>
```